Online retailer needs a Quirky yet professionally designed double sided business car

We mainly sell kitchen and home accessories but pretty much anything new and in demand. Have a look at our site and then come up with designs.
Design to be really catching and want people to visit the website.
Final details such as number, director name and email address will be given to the designer of the winning business card.

Www.zapvelbo.com

Ideas out of the norm also welcome!!

Industry/Entity Type

Business

```html
<!DOCTYPE html>
<html lang="en">
<head>
<meta charset="utf-8">
<title>Zapvelbo — Business Cards</title>
<link rel="stylesheet" href="https://fonts.googleapis.com/css2?family=Arimo:wght@400;700&display=swap">
<style>
  :root {
    --backdrop: #6f7074;
    --card-white: #ffffff;
    --card-orange: #f48a35;
    --ink-dark: #3b3b3d;
    --ink-grey: #5f6062;
    --accent-orange: #f07f1e;
    --rule-grey: #8a8a8c;
  }
  * { box-sizing: border-box; margin: 0; padding: 0; }
  html, body {
    width: 1200px; height: 901px; overflow: hidden;
    background: var(--backdrop);
    font-family: "Arimo", Arial, sans-serif;
  }
  .stage {
    width: 1200px; height: 901px;
    display: flex; align-items: center; justify-content: center; gap: 40px;
  }
  .card {
    position: relative; width: 540px; height: 309px; overflow: hidden;
    box-shadow: 0 10px 24px rgba(0,0,0,0.25);
  }
  .card--front { background: var(--card-white); color: var(--ink-grey); }
  .card--back { background: var(--card-orange); color: #ffffff; }
  .brand {
    position: absolute; left: 170px; top: 104px; width: 300px;
  }
  .brand__name {
    display: flex; align-items: center; gap: 10px;
    font-size: 44px; font-weight: 700; letter-spacing: 0.5px;
    color: var(--ink-dark); line-height: 1;
  }
  .card--back .brand__name { color: #ffffff; }
  .brand__dot {
    width: 16px; height: 16px; border-radius: 50%;
    background: var(--accent-orange); flex: none;
  }
  .card--back .brand__dot { background: #ffffff; }
  .brand__rule {
    margin-top: 8px; height: 1px; background: var(--rule-grey); width: 290px;
  }
  .card--back .brand__rule { background: rgba(255,255,255,0.8); }
  .brand__tagline {
    margin-top: 4px; margin-left: 40px;
    font-size: 14px; color: var(--accent-orange);
  }
  .card--back .brand__tagline { color: #ffffff; }
  .contact {
    position: absolute; left: 110px; top: 200px;
    font-size: 11.5px; line-height: 1.35;
  }
  .contact__name { font-size: 14px; margin-bottom: 8px; }
</style>
</head>
<body>
<main class="stage">
  <section class="card card--front" aria-label="Business card front">
    <div class="brand">
      <div class="brand__name"><span class="brand__dot"></span>Zapvelbo</div>
      <div class="brand__rule"></div>
      <div class="brand__tagline">home finds, fresh daily</div>
    </div>
    <div class="contact">
      <p class="contact__name">Marcus Lenne</p>
      <p>12, Harlow Lane,</p>
      <p>Ridgefield, NSW,</p>
      <p>Ph. 00 0412 5531 , Mob. 0412 553 1208</p>
      <p>www.zapvelbo.au, info@zapvelbo.au</p>
    </div>
  </section>

  <section class="card card--back" aria-label="Business card back">
    <div class="brand">
      <div class="brand__name"><span class="brand__dot"></span>Zapvelbo</div>
      <div class="brand__rule"></div>
      <div class="brand__tagline">home finds, fresh daily</div>
    </div>
    <div class="contact">
      <p class="contact__name">Marcus Lenne</p>
      <p>12, Harlow Lane,</p>
      <p>Ridgefield, NSW,</p>
      <p>Ph. 00 0412 5531 , Mob. 0412 553 1208</p>
      <p>www.zapvelbo.au, info@zapvelbo.au</p>
    </div>
  </section>
</main>
</body>
</html>
```